Quorvia medical teaching of the future

responsive website, onepager, for medical technology company. It has to look clean and high tech.

Look & feel
• Responsive
• Clean
• Combination icons + foto's
• Integration of a YouTube video

Landingpage items

• Header: picture + 'a video-based teaching platform for surgical procedures'
• About Deferred live medical teaching: Short description
• Features
o Video
o Teaching platform

• Benefits:
o More effective learning
o Faster sharing of knowledge & tecniques
o More cost effective

• References

• Products:
o Live (+link to more info)
o bTamo (+ link to more info)
o bTamo local (+link to more info)
o bTamo cloud (+ link to more info)

• Solutions:
o For medical device companies (+link to more info)
o Doctor and surgeons (+link to more info)
o Medical conferences (+link to more info)

Target Market(s)

medical device companies
surgeons and doctors
conference organisers

Industry/Entity Type

It Company

Number of Pages Required

1 page

Requirements
Must have
• Landingpage items
• • Header: picture + 'a video-based teaching platform for surgical procedures'
• • About Deferred live medical teaching: Short description
• • Features
• o Video
• o Teaching platform
• • Benefits:
• o More effective learning
• o Faster sharing of knowledge & tecniques
• o More cost effective
• • References
• • Products:
• o Live (+link to more info)
• o bTamo (+ link to more info)
• o bTamo local (+link to more info)
• o bTamo cloud (+ link to more info)
• • Solutions:
• o For medical device companies (+link to more info)
• o Doctor and surgeons (+link to more info)
• o Medical conferences (+link to more info)
Nice to have
• possibilty to show video

```html
<!DOCTYPE html>
<html lang="en">
<head>
<meta charset="utf-8">
<title>Quorvia – medical teaching of the future</title>
<link rel="stylesheet" href="https://fonts.googleapis.com/css2?family=Lato:wght@300;400;700;900&family=Montserrat:wght@400;700&display=swap">
<style>
:root{
  --teal:#2aa79a;
  --teal-dark:#1f8b80;
  --ink:#222;
  --text:#333;
  --topbar:#1c1c1c;
  --footer:#2e2e2e;
  --footer-text:#d8d8d8;
  --band:#f2f2f2;
  --white:#fff;
}
*{margin:0;padding:0;box-sizing:border-box}
html,body{width:1200px;height:3468px;overflow:hidden}
body{position:relative;background:var(--white);font-family:'Lato',sans-serif;color:var(--text)}
.section{position:absolute;left:0;width:1200px}
.btn{position:absolute;display:block;width:202px;height:45px;line-height:45px;text-align:center;background:var(--teal);color:var(--white);font-size:18px;text-decoration:none}

/* top bar */
.topbar{top:0;height:35px;background:var(--topbar);color:#ccc;font-size:11px}
.topbar span{position:absolute;top:11px}

/* header */
.site-header{top:35px;height:131px;background:var(--white)}
.brand{position:absolute;left:80px;top:36px;display:flex;align-items:center;gap:14px;color:var(--teal);font-size:44px;font-weight:400;text-decoration:none}
.brand i{display:block;width:46px;height:46px;border-radius:50%;background:var(--teal)}
.nav a{position:absolute;top:59px;font-size:16px;letter-spacing:1px;color:#333;text-decoration:none;text-transform:uppercase}
.nav a.active{border-bottom:2px solid var(--teal);padding-bottom:6px}
.menu-toggle{position:absolute;left:1118px;top:62px}

/* hero */
.hero{top:166px;height:620px}
.hero-photo{position:absolute;inset:0;background:linear-gradient(110deg,#5d6f73 0%,#3d5357 35%,#6f8a8c 60%,#2b3d42 100%)}
.hero-shade{position:absolute;inset:0;background:linear-gradient(90deg,rgba(0,0,0,.35),rgba(0,0,0,0) 60%)}
.hero h1{position:absolute;left:88px;top:248px;font-family:'Montserrat',sans-serif;font-weight:700;font-size:46px;color:var(--white);letter-spacing:1px}
.hero h2{position:absolute;left:88px;top:302px;font-weight:400;font-size:37px;color:var(--white);letter-spacing:1px}
.hero p{position:absolute;left:90px;top:358px;width:450px;font-size:18px;line-height:26px;color:var(--white);font-weight:700}
.hero .btn{left:90px;top:424px}
.hero-cut{position:absolute;left:0;bottom:0}

/* features band */
.features{top:786px;height:266px;background:var(--band)}
.feature-icon{position:absolute;top:69px;width:106px;height:111px;background:var(--teal);box-shadow:0 2px 4px rgba(0,0,0,.2)}
.feature-icon svg{position:absolute;left:23px;top:25px}
.feature h3{position:absolute;top:80px;font-size:17px;font-weight:700;color:var(--ink);letter-spacing:.5px}
.feature ul{position:absolute;top:104px;list-style:none;font-size:12.5px;line-height:19.5px;color:#333;text-transform:uppercase}
.feature li svg{vertical-align:-2px;margin-left:4px}

/* about */
.about{top:1052px;height:368px;text-align:center}
.section-title{font-weight:400;font-size:31px;color:var(--ink);letter-spacing:1px}
.about .section-title{position:absolute;left:0;width:1200px;top:66px}
.rule{position:absolute;height:3px;background:var(--ink)}
.about p{position:absolute;left:90px;width:1020px;font-size:17px;line-height:24px;color:#333}
.about .btn{left:502px;top:242px}

/* deferred teaching */
.deferred{top:1380px;height:600px}
.photo-wash{position:absolute;inset:0;background:linear-gradient(100deg,#c9d3d3 0%,#e3e9e8 40%,#d1dadb 70%,#b8c5c6 100%)}
.photo-veil{position:absolute;inset:0;background:rgba(255,255,255,.62)}
.deferred h2{position:absolute;left:96px;top:108px;font-weight:400;font-size:34px;color:var(--ink);letter-spacing:.5px}
.deferred p{position:absolute;left:97px;width:1040px;font-size:17px;line-height:24px;color:#222}
.deferred .btn{left:162px;top:382px}

/* video platform */
.platform{top:1954px;height:554px}
.platform .section-title{position:absolute;left:104px;top:56px;font-size:31px;text-transform:uppercase}
.platform .text{position:absolute;left:97px;top:134px;width:490px;font-size:16.5px;line-height:23px;color:#222}
.platform .btn{left:97px;top:464px}
.video{position:absolute;left:624px;top:136px;width:520px;height:356px;background:#fff;box-shadow:0 6px 14px rgba(0,0,0,.3)}
.video-frame{position:absolute;left:0;top:0;width:520px;height:330px;background:linear-gradient(120deg,#8d9aa3 0%,#c7cfd4 35%,#5f7d96 60%,#3f5a6e 100%)}
.video-play{position:absolute;left:228px;top:130px}
.video-bar{position:absolute;left:0;top:330px;width:520px;height:26px;background:linear-gradient(#e6e6e6,#bdbdbd)}

/* market size */
.market{top:2508px;height:447px}
.market h2{position:absolute;left:97px;top:44px;font-weight:400;font-size:31px;color:var(--ink);text-transform:uppercase;letter-spacing:.5px}
.market p{position:absolute;left:97px;top:118px;width:1048px;font-size:16.3px;line-height:20.5px;color:#222}
.market .btn{left:92px;top:354px}

/* footer */
.site-footer{top:2955px;height:435px;background:var(--footer);color:var(--footer-text)}
.footer-col{position:absolute;top:48px}
.footer-col h4{font-size:24px;font-weight:400;color:var(--white);line-height:32px}
.footer-col .line{width:54px;height:3px;background:var(--teal);margin-top:16px}
.footer-col ul{list-style:none;margin-top:42px;font-size:14px;line-height:40px}
.footer-col li:before{content:"›";color:#aaa;margin-right:12px}
.contact-line{position:absolute;left:58px;display:flex;gap:14px;align-items:flex-start;font-size:14px}
.form label{display:block;font-size:13px;margin-bottom:6px}
.form label b{color:#e33;font-weight:400}
.form .field{width:235px;height:32px;background:#2a2a2a;border:1px solid #555;margin-bottom:14px}
.form .area{height:72px}
.form .submit{display:inline-block;margin-top:18px;width:100px;height:34px;line-height:34px;background:var(--white);color:#333;text-align:center;font-size:13px}

.copyright{top:3390px;height:78px;text-align:center;font-size:14px;line-height:78px;color:#555;letter-spacing:.5px}
.copyright b{color:#222}
</style>
</head>
<body>

<div class="section topbar">
  <span style="left:84px">88 Harbor Lane, BC &nbsp;(555) 014-2210</span>
  <span style="left:564px">(555) 014-2290</span>
</div>

<header class="section site-header">
  <a class="brand" href="#"><i></i>Quorvia</a>
  <nav class="nav">
    <a class="active" href="#" style="left:490px">Home</a>
    <a href="#" style="left:578px">About us</a>
    <a href="#" style="left:717px">Product</a>
    <a href="#" style="left:855px">Solutions</a>
    <a href="#" style="left:1008px">Contact</a>
  </nav>
  <svg class="menu-toggle" width="26" height="18" viewBox="0 0 26 18"><g stroke="#2aa79a" stroke-width="2.5"><line x1="0" y1="2" x2="26" y2="2"/><line x1="0" y1="9" x2="26" y2="9"/><line x1="0" y1="16" x2="26" y2="16"/></g></svg>
</header>

<section class="section hero">
  <div class="hero-photo" role="img" aria-label="Surgeons in green scrubs operating under monitors in an operating room"></div>
  <div class="hero-shade"></div>
  <h1>WE ARE EXPERT</h1>
  <h2>IN THE FIELD OF MEDICAL!</h2>
  <p>Lorem Ipsum is simply dummy text of the printing and typesetting industry.</p>
  <a class="btn" href="#">Read More</a>
  <svg class="hero-cut" width="1200" height="90" viewBox="0 0 1200 90"><polygon points="0,90 1200,10 1200,90" fill="#f2f2f2"/></svg>
</section>

<section class="section features">
  <div class="feature">
    <div class="feature-icon" style="left:74px">
      <svg width="60" height="60" viewBox="0 0 60 60" fill="none" stroke="#fff" stroke-width="2.5" stroke-linejoin="round"><path d="M30 50 C10 36 6 26 10 18 C14 10 25 10 30 19 C35 10 46 10 50 18 C54 26 50 36 30 50Z"/><polyline points="2,31 18,31 22,24 27,38 31,28 35,31 58,31"/></svg>
    </div>
    <h3 style="left:199px">BENEFITS</h3>
    <ul style="left:199px">
      <li>More effective learning<svg width="14" height="14" viewBox="0 0 14 14"><circle cx="7" cy="7" r="7" fill="#1f8b80"/><path d="M5 4l3.5 3L5 10" stroke="#fff" stroke-width="1.6" fill="none"/></svg></li>
      <li>Faster sharing of knowledge</li>
      <li>&amp; tecniques more cost effective<svg width="14" height="14" viewBox="0 0 14 14"><circle cx="7" cy="7" r="7" fill="#1f8b80"/><path d="M5 4l3.5 3L5 10" stroke="#fff" stroke-width="1.6" fill="none"/></svg></li>
      <li>References<svg width="14" height="14" viewBox="0 0 14 14"><circle cx="7" cy="7" r="7" fill="#1f8b80"/><path d="M5 4l3.5 3L5 10" stroke="#fff" stroke-width="1.6" fill="none"/></svg></li>
    </ul>
  </div>
  <div class="feature">
    <div class="feature-icon" style="left:492px">
      <svg width="60" height="60" viewBox="0 0 60 60" fill="none" stroke="#fff" stroke-width="2.5"><rect x="14" y="8" width="32" height="46" rx="2"/><rect x="23" y="4" width="14" height="8" fill="#2aa79a"/><path d="M30 24v16M22 32h16"/></svg>
    </div>
    <h3 style="left:617px">PRODUCTS</h3>
    <ul style="left:617px">
      <li>Live<svg width="14" height="14" viewBox="0 0 14 14"><circle cx="7" cy="7" r="7" fill="#1f8b80"/><path d="M5 4l3.5 3L5 10" stroke="#fff" stroke-width="1.6" fill="none"/></svg></li>
      <li>bTamo<svg width="14" height="14" viewBox="0 0 14 14"><circle cx="7" cy="7" r="7" fill="#1f8b80"/><path d="M5 4l3.5 3L5 10" stroke="#fff" stroke-width="1.6" fill="none"/></svg></li>
      <li>bTamo local<svg width="14" height="14" viewBox="0 0 14 14"><circle cx="7" cy="7" r="7" fill="#1f8b80"/><path d="M5 4l3.5 3L5 10" stroke="#fff" stroke-width="1.6" fill="none"/></svg></li>
      <li>bTamo cloud<svg width="14" height="14" viewBox="0 0 14 14"><circle cx="7" cy="7" r="7" fill="#1f8b80"/><path d="M5 4l3.5 3L5 10" stroke="#fff" stroke-width="1.6" fill="none"/></svg></li>
    </ul>
  </div>
  <div class="feature">
    <div class="feature-icon" style="left:809px">
      <svg width="60" height="60" viewBox="0 0 60 60" fill="none" stroke="#fff" stroke-width="2.5" stroke-linejoin="round"><path d="M8 14h16l4 5h24v29H8z"/><path d="M30 26v14M23 33h14"/></svg>
    </div>
    <h3 style="left:934px">SOLUTIONS</h3>
    <ul style="left:934px">
      <li>For medical device<svg width="14" height="14" viewBox="0 0 14 14"><circle cx="7" cy="7" r="7" fill="#1f8b80"/><path d="M5 4l3.5 3L5 10" stroke="#fff" stroke-width="1.6" fill="none"/></svg></li>
      <li>companies<svg width="14" height="14" viewBox="0 0 14 14"><circle cx="7" cy="7" r="7" fill="#1f8b80"/><path d="M5 4l3.5 3L5 10" stroke="#fff" stroke-width="1.6" fill="none"/></svg></li>
      <li>Doctor and surgeons</li>
      <li>Medical conferences<svg width="14" height="14" viewBox="0 0 14 14"><circle cx="7" cy="7" r="7" fill="#1f8b80"/><path d="M5 4l3.5 3L5 10" stroke="#fff" stroke-width="1.6" fill="none"/></svg></li>
    </ul>
  </div>
</section>

<section class="section about">
  <h2 class="section-title">ABOUT US</h2>
  <div class="rule" style="left:530px;top:106px;width:68px"></div>
  <p style="top:132px">Quorvia is building a video based cloud teaching platform for all kinds of medical procedures using &nbsp;synchronized high resolution 360° and wide angle videos in a virtual reality environment.</p>
  <p style="top:204px">Quorvia changes the way medical procedures are taught.</p>
  <a class="btn" href="#">Read More</a>
</section>

<section class="section deferred">
  <div class="photo-wash" role="img" aria-label="Faded view of an operating room with surgical equipment"></div>
  <div class="photo-veil"></div>
  <svg style="position:absolute;left:0;top:0" width="1200" height="60" viewBox="0 0 1200 60"><polygon points="0,0 1200,0 0,60" fill="#fff"/></svg>
  <svg style="position:absolute;left:0;bottom:0" width="1200" height="70" viewBox="0 0 1200 70"><polygon points="1200,0 1200,70 0,70" fill="#fff"/></svg>
  <h2>Deferred Live Medical Teaching</h2>
  <p style="top:172px">Almost daily medical device companies, doctors and &nbsp;surgeons all over the world develop new or breakthrough products, medical and surgical techniques. These techniques save lives or increase the survival &nbsp;rate of some patients.</p>
  <p style="top:250px">1) <b>It is very costly</b>: flight fares, 5 star hotels, exclusive &nbsp;diners, ...<br>2) <b>Low ROI</b>: only 20 to 30% starts using the presented &nbsp;tools and techniques.<br>3) <b>Low quality</b>: with many people in the OR visiting surgeons don't have a clear and detailed view on the procedure.</p>
  <a class="btn" href="#">Read More</a>
</section>

<section class="section platform">
  <h2 class="section-title">A video based teaching platform for &nbsp;medical procedures</h2>
  <div class="rule" style="left:104px;top:96px;width:40px"></div>
  <div class="text">
    Quorvia is a video based cloud teaching platform for medical procedures using self-captured synchronized high resolution 360° and wide angle videos in a virtual reality environment.<br><br>
    1) Immersive cloud based teaching platform.<br>
    2) Based on high resolution wide-angle 360° video capturing of surgical procedures<br>
    3) Multiple synchronized cameras<br>
    4) A single person performs capturing with no need to access the OR<br>
    5) Captured content will be made available as a cloud service on PC, tablets and smartphones for educational &nbsp;and research purposes.
  </div>
  <a class="btn" href="#">Read More</a>
  <div class="video">
    <div class="video-frame" role="img" aria-label="Video still of a surgical team in an operating room with imaging equipment"></div>
    <svg class="video-play" width="60" height="60" viewBox="0 0 60 60"><polygon points="12,6 54,30 12,54" fill="#fff"/></svg>
    <div class="video-bar">
      <svg width="520" height="26" viewBox="0 0 520 26"><g fill="#333"><polygon points="12,8 20,13 12,18"/><rect x="30" y="8" width="3" height="10"/><polygon points="40,13 46,8 46,18"/><polygon points="58,8 64,13 58,18"/><rect x="90" y="11" width="300" height="4" fill="#888"/><rect x="90" y="11" width="40" height="4"/><rect x="420" y="9" width="8" height="8"/><rect x="440" y="11" width="60" height="4" fill="#888"/></g></svg>
    </div>
  </div>
</section>

<section class="section market">
  <div class="photo-wash" role="img" aria-label="Faded view of an operating room with lights and instruments"></div>
  <div class="photo-veil"></div>
  <h2>Market size</h2>
  <p>1. Teaching surgeons who want to spread their knowledge to other surgeons on a very short term basis.<br>2. The medical device companies who develop the latest and revolutionary equipment. In over 75%, as we know it, healthcare companies sponsor these teaching sessions. Healthcare companies contact top surgeons to do teaching sessions with their appliances/equipment and pay them generous for these teaching sessions. For the companies it is important that as many as possible hospitals and surgeons use their products. By teaching how to use them properly will increase their business. They are already investing millions in teaching sessions in the hospitals. By using our 360° immersive capture unit, they will have more and better exposure in the OR and outside on the screens, during conferences or by using our platform for distant teaching. It is the perfect way to learn young surgeons and nurses to work with their equipment and appliances.</p>
  <a class="btn" href="#">Read More</a>
</section>

<footer class="section site-footer">
  <div class="footer-col" style="left:58px">
    <h4 style="font-weight:700">Quorvia<br>Information</h4>
    <div class="line"></div>
  </div>
  <div class="contact-line" style="top:160px">
    <svg width="16" height="22" viewBox="0 0 16 22"><path d="M8 0C3.6 0 0 3.5 0 7.8 0 13 8 22 8 22s8-9 8-14.2C16 3.5 12.4 0 8 0z" fill="#2aa79a"/><circle cx="8" cy="8" r="3" fill="#2e2e2e"/></svg>
    <div><div style="font-size:14px">Halvern Ltd.</div><div style="font-size:11px;line-height:14px;margin-top:4px">88 Harbor Lane, Country<br>BC (555) 014-2210</div></div>
  </div>
  <div class="contact-line" style="top:284px">
    <svg width="14" height="20" viewBox="0 0 14 20"><rect x="1" y="0" width="12" height="20" rx="2" fill="#2aa79a"/><rect x="3" y="3" width="8" height="12" fill="#2e2e2e"/></svg>
    <div style="font-size:16px">(555) 014-2210</div>
  </div>
  <div class="contact-line" style="top:320px">
    <svg width="18" height="14" viewBox="0 0 18 14"><rect width="18" height="14" fill="#2aa79a"/><path d="M0 0l9 7 9-7" stroke="#2e2e2e" stroke-width="1.5" fill="none"/></svg>
    <div style="font-size:16px">info@quorvia.com</div>
  </div>

  <div class="footer-col" style="left:340px">
    <h4>Doctors</h4>
    <div class="line"></div>
    <ul>
      <li>Dr. Elena Marsh</li><li>Dr. Owen Patel</li><li>Dr. Lucas Brandt</li><li>Dr. Martin Okafor</li><li>Dr. Paul Varga</li><li>Dr. Irene Hollis</li>
    </ul>
  </div>
  <div class="footer-col" style="left:620px">
    <h4>Services</h4>
    <div class="line"></div>
    <ul>
      <li>Pediatric Clinic</li><li>Diagnosis Clinic</li><li>Cardiac Clinic</li><li>Laboratory Analysis</li><li>Dental Clinic</li><li>Gynecological Clinic</li>
    </ul>
  </div>
  <div class="footer-col form" style="left:902px">
    <h4>Quick Contacts</h4>
    <div class="line" style="margin-bottom:58px"></div>
    <label>Your Email <b>*</b></label>
    <div class="field"></div>
    <label>Your message <b>*</b></label>
    <div class="field area"></div>
    <span class="submit">Submit</span>
  </div>
</footer>

<div class="section copyright">Copyright 2017 <b>Quorvia</b>. All right reserved</div>

</body>
</html>
```